Business Card Design

I would like a new business card design for an accounting firm that specializes in resolving clients tax problems. I want the card to give the impression that we are not your typical stodgy accounting firm, but at the same time we will get the job done.
Industry/Entity Type
Business
Contact Information for Business Card
Dorian T Welsby
Certified Public Accountant
38-27 52nd Street
Sunnyside, NY 11287
Tel: (718) 555-0142
Fax: (888) 555-0199
e-mail: dtwthecpa@ledgerpost.com
website: harborfilingreliefexperts.com

```html
<!DOCTYPE html>
<html lang="en">
<head>
<meta charset="utf-8">
<title>Dorian T Welsby — Business Card</title>
<link rel="stylesheet" href="https://fonts.googleapis.com/css2?family=Libre+Baskerville:wght@700&family=Arimo:wght@400;700&display=swap">
<style>
  :root {
    --page-bg: #e9e6e1;
    --card-white: #ffffff;
    --navy: #153f73;
    --navy-deep: #0f315d;
    --navy-light: #3f679a;
    --gold: #f6c12c;
    --gold-deep: #e3a812;
    --ink-gray: #8a8c8f;
    --text-light: #ffffff;
  }
  * { margin: 0; padding: 0; box-sizing: border-box; }
  html, body {
    width: 1200px;
    height: 1023px;
    overflow: hidden;
    background: var(--page-bg);
  }
  .stage {
    position: relative;
    width: 1200px;
    height: 1023px;
  }
  .card {
    position: absolute;
    left: 110px;
    top: 231px;
    width: 980px;
    height: 560px;
    border-radius: 4px;
    overflow: hidden;
    background: var(--card-white);
    box-shadow: 0 10px 30px rgba(0,0,0,0.18);
  }
  .card-shapes {
    position: absolute;
    inset: 0;
  }
  .identity {
    position: absolute;
    left: 70px;
    top: 78px;
  }
  .identity-name {
    font-family: "Libre Baskerville", Georgia, serif;
    font-weight: 700;
    font-size: 66px;
    letter-spacing: 1px;
    color: var(--navy);
    line-height: 1;
    text-transform: uppercase;
  }
  .identity-title {
    margin-top: 14px;
    padding-left: 90px;
    font-family: "Arimo", Arial, sans-serif;
    font-weight: 700;
    font-size: 22px;
    letter-spacing: 3px;
    color: var(--ink-gray);
    text-transform: uppercase;
  }
  .address {
    position: absolute;
    left: 70px;
    bottom: 70px;
    font-family: "Arimo", Arial, sans-serif;
    font-size: 25px;
    line-height: 1.5;
    letter-spacing: 1px;
    color: var(--text-light);
  }
  .contacts {
    position: absolute;
    left: 470px;
    top: 318px;
    list-style: none;
    font-family: "Arimo", Arial, sans-serif;
    font-size: 25px;
    letter-spacing: 1px;
    color: var(--text-light);
  }
  .contact-item {
    display: flex;
    align-items: center;
    gap: 14px;
    height: 42px;
  }
  .contact-icon {
    width: 22px;
    height: 22px;
    flex: none;
  }
</style>
</head>
<body>
<main class="stage">
  <article class="card">
    <svg class="card-shapes" width="980" height="560" viewBox="0 0 980 560" aria-hidden="true">
      <defs>
        <linearGradient id="navyFill" x1="0" y1="0" x2="1" y2="1">
          <stop offset="0" stop-color="#1d4a82"/>
          <stop offset="0.5" stop-color="#153f73"/>
          <stop offset="1" stop-color="#0f315d"/>
        </linearGradient>
        <linearGradient id="goldFill" x1="0" y1="0" x2="1" y2="0">
          <stop offset="0" stop-color="#e3a812"/>
          <stop offset="1" stop-color="#f8ca3c"/>
        </linearGradient>
      </defs>
      <path class="band-gold" d="M0 268 C 300 300, 650 270, 980 150 L 980 560 L 0 560 Z" fill="url(#goldFill)"/>
      <path class="band-navy" d="M0 286 C 300 316, 660 292, 980 184 L 980 560 L 0 560 Z" fill="url(#navyFill)"/>
      <path class="band-edge" d="M0 268 C 300 300, 650 270, 980 150" fill="none" stroke="#1b3e6b" stroke-width="2"/>
    </svg>

    <header class="identity">
      <h1 class="identity-name">Dorian T.Welsby</h1>
      <p class="identity-title">Certified Public Accountant</p>
    </header>

    <address class="address">
      38-27 52nd Street<br>
      Sunnyside, NY 11287
    </address>

    <ul class="contacts">
      <li class="contact-item">
        <svg class="contact-icon" viewBox="0 0 22 22" aria-label="Telephone">
          <rect width="22" height="22" rx="4" fill="var(--gold)"/>
          <path d="M7 5h3l1 4-2 1.5a8 8 0 0 0 3.5 3.5L14 12l4 1v3c0 1-1 1.5-2 1.5A12 12 0 0 1 5 7c0-1 .5-2 2-2z" fill="var(--navy-deep)"/>
        </svg>
        <span>(718) 555-0142</span>
      </li>
      <li class="contact-item">
        <svg class="contact-icon" viewBox="0 0 22 22" aria-label="Fax">
          <rect width="22" height="22" rx="4" fill="var(--gold)"/>
          <rect x="7" y="4" width="8" height="5" fill="var(--navy-deep)"/>
          <rect x="4" y="9" width="14" height="7" rx="1" fill="var(--navy-deep)"/>
          <rect x="7" y="14" width="8" height="4" fill="var(--navy-deep)"/>
        </svg>
        <span>(888) 555-0199</span>
      </li>
      <li class="contact-item">
        <svg class="contact-icon" viewBox="0 0 22 22" aria-label="Email">
          <rect width="22" height="22" rx="4" fill="var(--gold)"/>
          <rect x="4" y="6" width="14" height="10" fill="var(--navy-deep)"/>
          <path d="M4 6l7 6 7-6" fill="none" stroke="var(--gold)" stroke-width="1.4"/>
        </svg>
        <span>dtwthecpa@ledgerpost.com</span>
      </li>
      <li class="contact-item">
        <svg class="contact-icon" viewBox="0 0 22 22" aria-label="Website">
          <rect width="22" height="22" rx="4" fill="var(--gold)"/>
          <circle cx="11" cy="11" r="6.5" fill="none" stroke="var(--navy-deep)" stroke-width="1.6"/>
          <path d="M4.5 11h13M11 4.5c-3 3.5-3 9.5 0 13M11 4.5c3 3.5 3 9.5 0 13" fill="none" stroke="var(--navy-deep)" stroke-width="1.3"/>
        </svg>
        <span>harborfilingreliefexperts.com</span>
      </li>
    </ul>
  </article>
</main>
</body>
</html>
```